THE MARKETPLACE FOR WAREHOUSE, the new way of doing logistics

We need an avant-garde, modern, minimalist and elegant web design for our company called VORDEN. This company represents the future of logistics, where users can find multiple offers of spaces (warehouse) in one place and other users can offer their available spaces to generate an extra cash inflow. A sample of this company is www.plindo-example.com, a US company that has developed this business. The closest thing to this type of business is NESTLOO, since it develops a similar model for people who offer spaces in their homes and people who need a space for a limited time. My domain site is www.vorden-example.com, where is the logo of my company. spanish- ------------------------------------------------ ---------------------------------------------- We need a web design avant-garde, modern, minimalist and elegant for our company called VORDEN. This company represents the future of logistics, where users can find multiple offers of spaces (wineries) in one place and other users can offer their available spaces to generate an extra profit. A sample of this company is www.plindo-example.com, a US company that has developed this business. The closest thing to this type of business is NESTLOO, since it develops a similar model for people who offer spaces in their homes and people who need a space for a limited time. My domain site is www.vorden-example.com, where is the logo of my company.

Target Market(s)

Companies, entrepreneurs, Companies, entrepreneurs,

Industry/Entity Type

Logistic

Number of Pages Required

5+ page

Colors
0d5aa6
ffffff
000000

Requirements
Must have
• A sober and minimalist homepage type quorbit, NstLoo. That is intuitive, must have spaces for advertising banners. You must always highlight the company logo. A sober and minimalist homepage like quorbit, NstLoo. That is intuitive, must have spaces for advertising banners. Must always highlight the company logo.

```html
<!DOCTYPE html>
<html lang="en">
<head>
<meta charset="utf-8">
<title>VORDEN – On-Demand Warehousing</title>
<link rel="stylesheet" href="https://fonts.googleapis.com/css2?family=Roboto:wght@300;400;500;700;900&family=Open+Sans:wght@400;600&display=swap">
<style>
:root{
  --blue:#0d5aa6;
  --blue-deep:#0b4a93;
  --blue-light:#e8f1fa;
  --ink:#1b1b1b;
  --text:#555b63;
  --muted:#8a9099;
  --grey-band:#f1f2f4;
  --card:#f7f7f8;
  --white:#ffffff;
  --black:#000000;
  --footer:#121316;
  --accent:#e9432c;
  --star:#f5b91b;
}
*{box-sizing:border-box;margin:0;padding:0}
html,body{width:1200px;height:4945px;overflow:hidden}
body{position:relative;background:var(--white);font-family:'Open Sans',sans-serif;color:var(--text)}
.abs{position:absolute}
h1,h2,h3,h4,.heading{font-family:'Roboto',sans-serif}

/* Hero */
.hero{position:absolute;left:0;top:0;width:1200px;height:680px;overflow:hidden}
.hero-photo{position:absolute;inset:0;background:linear-gradient(180deg,#2a2d33 0%,#4a4236 40%,#3a3530 70%,#1d2633 100%)}
.hero-shade{position:absolute;inset:0;background:linear-gradient(180deg,rgba(8,14,26,.55),rgba(8,14,26,.35) 50%,rgba(8,14,26,.6))}
.hero-edge{position:absolute;left:0;top:0}
.nav{position:absolute;left:0;top:0;width:1200px;height:130px}
.brand{position:absolute;display:flex;align-items:center;gap:10px}
.brand-mark{width:46px;height:46px;border-radius:50%;border:4px solid var(--blue)}
.brand-name{font-family:'Roboto',sans-serif;font-weight:900;font-size:34px;letter-spacing:1px;line-height:1}
.brand-tag{font-family:'Roboto',sans-serif;font-size:9px;letter-spacing:2px;margin-top:3px}
.nav .brand{left:132px;top:38px;color:var(--white)}
.menu{position:absolute;left:550px;top:50px;display:flex;gap:32px;font-family:'Roboto',sans-serif;font-size:15px;font-weight:500;color:var(--white);text-transform:uppercase;letter-spacing:.5px}
.menu .home{text-transform:none}
.sign-in{position:absolute;left:956px;top:42px;width:110px;height:34px;border:2px solid var(--white);border-radius:17px;color:var(--white);font:500 14px 'Roboto',sans-serif;display:flex;align-items:center;justify-content:center;gap:6px;text-transform:uppercase}
.hero-title{position:absolute;left:0;width:1200px;top:228px;text-align:center;color:var(--white);font:900 42px 'Roboto',sans-serif;letter-spacing:.5px}
.hero-sub{position:absolute;left:0;width:1200px;top:305px;text-align:center;color:var(--white);font:500 21px 'Roboto',sans-serif}
.hero-btn{position:absolute;top:366px;width:164px;height:44px;border:2px solid var(--white);border-radius:22px;color:var(--white);font:500 15px 'Roboto',sans-serif;display:flex;align-items:center;justify-content:center;letter-spacing:.5px}
.dots{position:absolute;left:568px;top:497px;display:flex;gap:8px}
.dots span{width:13px;height:13px;border-radius:50%;border:2px solid var(--white)}
.dots span.on{background:var(--white)}

/* Services */
.service{position:absolute;top:768px;width:185px;height:158px;background:var(--white);border:1px solid #d9dce0;border-radius:4px;box-shadow:0 3px 8px rgba(0,0,0,.12);text-align:center;font:400 16px 'Roboto',sans-serif;color:var(--ink);padding-top:22px}
.service svg{display:block;margin:0 auto 12px}
.service.active{background:var(--blue);color:var(--white);border-color:var(--blue)}
.service-title{position:absolute;left:0;width:1200px;top:978px;text-align:center;color:var(--blue);font:400 28px 'Roboto',sans-serif;display:flex;justify-content:center;align-items:center;gap:10px}
.service-copy{position:absolute;left:200px;width:805px;top:1046px;text-align:center;font-size:13px;line-height:1.75;color:var(--text)}

/* Report */
.report{position:absolute;left:0;top:1236px;width:1200px;height:512px;background:var(--grey-band)}
.laptop{position:absolute;left:132px;top:100px;width:462px;height:312px}
.laptop-screen{position:absolute;left:0;top:0;width:462px;height:290px;border-radius:10px;background:linear-gradient(160deg,#1b1f26,#12331f 55%,#0d1a14)}
.laptop-base{position:absolute;left:-14px;top:290px;width:490px;height:16px;border-radius:0 0 14px 14px;background:linear-gradient(180deg,#d6d8dc,#9ea3aa)}
.play{position:absolute;left:196px;top:110px}
.report-kicker{position:absolute;left:670px;top:120px;font:400 26px 'Roboto',sans-serif;color:var(--ink)}
.report-title{position:absolute;left:670px;top:153px;font:700 26px 'Roboto',sans-serif;color:var(--ink)}
.report-title em{font-style:normal;color:var(--blue)}
.report-copy{position:absolute;left:670px;top:200px;width:420px;font-size:14px;line-height:1.75}
.btn-outline{position:absolute;left:670px;top:372px;width:120px;height:36px;border:2px solid var(--blue);border-radius:18px;color:var(--blue);font:500 14px 'Roboto',sans-serif;display:flex;align-items:center;justify-content:center}

/* Solutions */
.solutions-title{position:absolute;left:0;width:1200px;top:1842px;text-align:center;font:700 27px 'Roboto',sans-serif;color:var(--ink)}
.solutions-title em{font-style:normal;color:var(--blue)}
.solutions-sub{position:absolute;left:0;width:1200px;top:1890px;text-align:center;font:400 25px 'Roboto',sans-serif;color:var(--ink);letter-spacing:.5px}
.ring{position:absolute;left:0;top:1940px}
.core{position:absolute;left:470px;top:2046px;width:260px;height:260px;border-radius:50%;border:10px solid var(--blue);display:flex;align-items:center;justify-content:center;font:900 40px 'Roboto',sans-serif;color:var(--blue);letter-spacing:1px}
.feature{position:absolute;width:280px;font-size:12.5px;line-height:1.6}
.feature h4{font:500 19px 'Roboto',sans-serif;color:var(--ink);margin-bottom:4px}
.feature.left{text-align:right}

/* Reviews */
.reviews{position:absolute;left:0;top:2522px;width:1200px;height:468px;background:var(--blue-deep)}
.reviews h2{position:absolute;left:0;width:1200px;top:110px;text-align:center;color:var(--white);font:500 30px 'Roboto',sans-serif}
.arrow-btn{position:absolute;top:250px;width:34px;height:34px;border-radius:50%;border:2px solid rgba(255,255,255,.8)}
.review{position:absolute;top:200px;width:320px;color:var(--white)}
.avatar{position:absolute;left:0;top:0;width:68px;height:68px;border-radius:50%;background:linear-gradient(160deg,#c9b8a6,#7c6c5e);border:3px solid var(--white)}
.review-body{position:absolute;left:88px;top:2px;width:230px}
.review-quote{font-size:12.5px;line-height:1.6;font-style:italic}
.review-quote b{font:900 22px 'Roboto',sans-serif;font-style:normal;vertical-align:-6px;margin-right:4px}
.review-name{font:700 10.5px 'Roboto',sans-serif;margin-top:10px;text-transform:uppercase;letter-spacing:.5px}
.review-role{font-size:10px;opacity:.85}
.stars{margin-top:16px;color:var(--star);font-size:18px;letter-spacing:2px}

/* Blog */
.blog-title{position:absolute;left:0;width:1200px;top:3124px;text-align:center;font:700 38px 'Roboto',sans-serif;color:var(--ink)}
.blog-title em{font-style:normal;color:var(--blue)}
.post{position:absolute;top:3208px;width:290px;height:320px;background:var(--card)}
.post-photo{height:182px}
.post-body{padding:20px 14px}
.post-body h3{font:500 16px 'Roboto',sans-serif;color:var(--ink)}
.post-meta{font-size:12px;color:var(--muted);margin:8px 0 10px;display:flex;align-items:center;gap:6px}
.post-body p{font-size:12px;line-height:1.6}

/* Search */
.search{position:absolute;left:0;top:3610px;width:636px;height:468px;background:var(--blue-light)}
.search h2{position:absolute;left:132px;top:106px;font:700 28px 'Roboto',sans-serif;color:var(--ink)}
.field{position:absolute;left:132px;width:402px;border-bottom:1px solid #6c737c;font:400 15px 'Roboto',sans-serif;color:var(--ink);padding-bottom:10px}
.btn-solid{position:absolute;left:132px;top:343px;width:138px;height:32px;background:var(--blue);color:var(--white);font:500 15px 'Roboto',sans-serif;display:flex;align-items:center;justify-content:center}
.map{position:absolute;left:636px;top:3610px;width:564px;height:468px;background:linear-gradient(135deg,#e4e4e2,#d3d4d1 50%,#e9e8e4)}

/* Partners */
.partner{position:absolute;top:4144px;height:92px;background:#f3f3f4;border:1px solid #e4e5e7;box-shadow:0 2px 5px rgba(0,0,0,.08);display:flex;align-items:center;justify-content:center;gap:8px;font:500 17px 'Roboto',sans-serif;color:#4a4f56}
.partner i{width:14px;height:14px;background:#6a6f76;display:block}

/* Footer */
.footer{position:absolute;left:0;top:4434px;width:1200px;height:511px;background:var(--footer);color:#c9ccd1}
.newsletter{position:absolute;left:132px;top:4296px;width:570px;height:227px;background:linear-gradient(135deg,#0d5aa6,#0a3f7d)}
.newsletter h2{position:absolute;left:0;width:570px;top:42px;text-align:center;font:700 34px 'Roboto',sans-serif;color:var(--white)}
.newsletter p{position:absolute;left:150px;width:270px;top:92px;text-align:center;font-size:14px;line-height:1.4;color:var(--white)}
.subscribe{position:absolute;left:40px;top:160px;width:500px;height:40px;border-radius:20px;background:var(--white);overflow:hidden}
.subscribe span{position:absolute;left:18px;top:12px;font-size:12px;color:var(--muted)}
.subscribe b{position:absolute;right:0;top:0;width:110px;height:40px;border-radius:20px;background:var(--accent);color:var(--white);font:700 13px 'Roboto',sans-serif;display:flex;align-items:center;justify-content:center}
.ad-slot{position:absolute;left:712px;top:4296px;width:353px;height:227px;background:var(--white);border:2px solid #dfe1e4;display:flex;align-items:center;justify-content:center;text-align:center;font:700 38px/1.1 'Roboto',sans-serif;color:var(--blue)}
.footer .brand{left:132px;top:176px;color:var(--white)}
.footer-about{position:absolute;left:132px;top:250px;width:300px;font-size:13px;line-height:1.7}
.col-title{position:absolute;top:158px;font:700 17px 'Roboto',sans-serif;color:var(--white);text-transform:uppercase}
.contact{position:absolute;left:504px;top:206px;font-size:13px;line-height:1.3}
.contact li{list-style:none;display:flex;gap:10px;align-items:flex-start;margin-bottom:16px}
.links{position:absolute;left:778px;top:206px;font-size:13px}
.links li{list-style:none;margin-bottom:9px}
.links li::before{content:"•";margin-right:8px}
.social{position:absolute;left:960px;top:206px;font-size:13px}
.social li{list-style:none;display:flex;align-items:center;gap:10px;margin-bottom:12px}
.social li i{width:24px;height:24px;border-radius:50%;border:1.5px solid #c9ccd1;display:block}
.footer-rule{position:absolute;left:0;top:428px;width:1200px;height:1px;background:#2a2c31}
.copyright{position:absolute;left:0;width:1200px;top:455px;text-align:center;font-size:12px}
</style>
</head>
<body>

<section class="hero">
  <div class="hero-photo" role="img" aria-label="Warehouse aisle with tall pallet racks and a glowing exit at the end"></div>
  <div class="hero-shade"></div>
  <svg class="hero-edge" width="1200" height="680" viewBox="0 0 1200 680">
    <polygon points="0,620 600,668 1200,620 1200,680 0,680" fill="#ffffff"/>
    <polyline points="0,604 600,652 1200,604" fill="none" stroke="#0d5aa6" stroke-width="16"/>
  </svg>
  <nav class="nav">
    <div class="brand">
      <span class="brand-mark"></span>
      <div><div class="brand-name">VORDEN</div><div class="brand-tag">ON-DEMAND WAREHOUSING</div></div>
    </div>
    <div class="menu"><span class="home">Home</span><span>Solutions</span><span>Company</span><span>Blog</span></div>
    <div class="sign-in">
      <svg width="12" height="13" viewBox="0 0 12 13"><circle cx="6" cy="3.5" r="3" fill="#fff"/><path d="M0 13c0-4 2.5-6 6-6s6 2 6 6z" fill="#fff"/></svg>Sign In
    </div>
  </nav>
  <h1 class="hero-title">FROM STARTUP TO SCALE</h1>
  <p class="hero-sub">eCommerce Order Fulfillment for Every Stage of Your Business</p>
  <div class="hero-btn" style="left:430px">FIND SPACE</div>
  <div class="hero-btn" style="left:606px">LIST SPACE</div>
  <div class="dots"><span class="on"></span><span></span><span></span></div>
</section>

<div class="service" style="left:185px">
  <svg width="56" height="56" viewBox="0 0 56 56" fill="none" stroke="#1b1b1b" stroke-width="2.5"><path d="M28 6 48 16v24L28 50 8 40V16z"/><path d="M8 16l20 10 20-10M28 26v24"/></svg>
  eCommerce<br>Fulfillment
</div>
<div class="service active" style="left:402px">
  <svg width="56" height="56" viewBox="0 0 56 56" fill="none" stroke="#fff" stroke-width="2.5"><path d="M6 22 28 8l22 14v26H6z"/><rect x="16" y="28" width="24" height="20"/><path d="M16 34h24M16 40h24"/></svg>
  Retail<br>Distribution
</div>
<div class="service" style="left:613px">
  <svg width="56" height="56" viewBox="0 0 56 56" fill="none" stroke="#1b1b1b" stroke-width="2.5"><path d="M6 20 28 8l22 12v28H6z"/><path d="M14 48V26h28v22M14 32h28M14 38h28M14 44h28"/></svg>
  Inventory<br>Overflow
</div>
<div class="service" style="left:828px">
  <svg width="56" height="56" viewBox="0 0 56 56" fill="none" stroke="#1b1b1b" stroke-width="2.5"><path d="M4 14h30v24H4zM34 22h10l8 8v8H34z"/><circle cx="14" cy="42" r="5"/><circle cx="42" cy="42" r="5"/></svg>
  Delivery
</div>

<h2 class="service-title">
  <svg width="28" height="26" viewBox="0 0 28 26" fill="none" stroke="#1b1b1b" stroke-width="2"><path d="M2 10 14 2l12 8v15H2z"/><rect x="7" y="14" width="14" height="11"/><path d="M7 18h14M7 22h14"/></svg>
  Retail Distribution
</h2>
<p class="service-copy">It is a long established fact that a reader will be distracted by the readable content of a page when looking at its layout. The point of using Lorem Ipsum is that it has a more-or-less normal distribution of letters, as opposed to using 'Content here, content here', making it look like readable English. Many desktop publishing packages and web page editors now use Lorem Ipsum as their default model text, and a search for 'lorem ipsum' will uncover many web sites still in their infancy.</p>

<section class="report">
  <div class="laptop">
    <div class="laptop-screen" role="img" aria-label="Laptop screen showing a green stock market chart video"></div>
    <div class="laptop-base"></div>
    <svg class="play" width="70" height="70" viewBox="0 0 70 70"><circle cx="35" cy="35" r="33" fill="#ffffff"/><polygon points="28,22 50,35 28,48" fill="#000000"/></svg>
  </div>
  <div class="report-kicker">WAREHOUSE CAPACITY</div>
  <div class="report-title">ECONOMICS &amp; <em>TRENDS REPORT</em></div>
  <p class="report-copy">Sed ut perspiciatis unde omnis iste natus error sit voluptatem accusantium doloremque laudantium, totam rem aperiam, eaque ipsa quae ab illo inventore veritatis et quasi architecto beatae vitae dicta sunt explicabo. Nemo enim ipsam</p>
  <div class="btn-outline">Read More</div>
</section>

<h2 class="solutions-title"><em>VORDEN SOLUTIONS</em> ARE MADE POSSIBLE BY</h2>
<p class="solutions-sub heading">A POWERFUL SOFTWARE PLATFORM</p>
<svg class="ring" width="1200" height="480" viewBox="0 1940 1200 480">
  <circle cx="600" cy="2176" r="208" fill="none" stroke="#0d5aa6" stroke-width="5"/>
  <g fill="#0d5aa6">
    <circle cx="435" cy="2057" r="36"/><circle cx="392" cy="2196" r="36"/><circle cx="452" cy="2328" r="36"/>
    <circle cx="758" cy="2057" r="36"/><circle cx="801" cy="2196" r="36"/><circle cx="742" cy="2328" r="36"/>
  </g>
  <g fill="none" stroke="#fff" stroke-width="2.5">
    <rect x="423" y="2045" width="9" height="9"/><rect x="438" y="2045" width="9" height="9"/><rect x="423" y="2060" width="9" height="9"/><rect x="438" y="2060" width="9" height="9"/>
    <path d="M392 2212c-8-10-12-16-12-22a12 12 0 0 1 24 0c0 6-4 12-12 22z"/><circle cx="392" cy="2190" r="4"/>
    <path d="M442 2314h14l6 6v22h-20z"/><path d="M447 2326h10M447 2332h10"/>
    <path d="M744 2070v-10M752 2070v-16M760 2070v-12M768 2070v-20M740 2072h34"/>
    <circle cx="801" cy="2196" r="15"/><path d="M786 2196h30M801 2181c-8 8-8 22 0 30M801 2181c8 8 8 22 0 30"/>
    <rect x="726" y="2316" width="32" height="22"/><path d="M730 2332l8-8 6 6 10-10"/>
  </g>
</svg>
<div class="core">VORDEN</div>
<div class="feature left" style="left:96px;top:2022px"><h4>Operations:</h4>Sed ut perspiciatis unde omnis iste natus error sit voluptatem accusantium doloremque laudantium</div>
<div class="feature left" style="left:60px;top:2160px"><h4>Matching:</h4>Sed ut perspiciatis unde omnis iste natus error sit voluptatem accusantium doloremque</div>
<div class="feature left" style="left:110px;top:2294px"><h4>Billing:</h4>Sed ut perspiciatis unde omnis iste natus error sit voluptatem accusantium doloremque laudantium</div>
<div class="feature" style="left:820px;top:2022px"><h4>Analytics</h4>Sed ut perspiciatis unde omnis iste natus error sit voluptatem accusantium doloremque laudantium</div>
<div class="feature" style="left:862px;top:2160px"><h4>Logistics Report</h4>Sed ut perspiciatis unde omnis iste natus error sit voluptatem accusantium doloremque</div>
<div class="feature" style="left:800px;top:2294px"><h4>Marketplace</h4>Sed ut perspiciatis unde omnis iste natus error sit voluptatem accusantium doloremque laudantium</div>

<section class="reviews">
  <h2>CLIENT REVIEWS</h2>
  <div class="arrow-btn" style="left:72px"><svg width="30" height="30" viewBox="0 0 30 30"><path d="M17 9l-6 6 6 6" fill="none" stroke="#fff" stroke-width="2"/></svg></div>
  <div class="arrow-btn" style="left:1104px"><svg width="30" height="30" viewBox="0 0 30 30"><path d="M13 9l6 6-6 6" fill="none" stroke="#fff" stroke-width="2"/></svg></div>
  <div class="review" style="left:132px">
    <div class="avatar" role="img" aria-label="Client portrait"></div>
    <div class="review-body">
      <p class="review-quote"><b>“</b>At vero eos et accusamus et iusto odio dignissimos ducimus qui blanditiis praesentium voluptatum deleniti atque.</p>
      <div class="review-name">Marla Fenwick</div><div class="review-role">Financial Services Professional</div>
      <div class="stars">★★★★☆</div>
    </div>
  </div>
  <div class="review" style="left:455px">
    <div class="avatar" role="img" aria-label="Client portrait"></div>
    <div class="review-body">
      <p class="review-quote"><b>“</b>At vero eos et accusamus et iusto odio dignissimos ducimus qui blanditiis praesentium voluptatum deleniti atque.</p>
      <div class="review-name">Oren T. Calloway</div><div class="review-role">National Urban Fellow at the Foundation</div>
      <div class="stars">★★★★½</div>
    </div>
  </div>
  <div class="review" style="left:778px">
    <div class="avatar" role="img" aria-label="Client portrait"></div>
    <div class="review-body">
      <p class="review-quote"><b>“</b>At vero eos et accusamus et iusto odio dignissimos ducimus qui blanditiis praesentium voluptatum deleniti atque.</p>
      <div class="review-name">Jules Braddock</div><div class="review-role">Content Strategist | Entrepreneur &amp; Upcoming</div>
      <div class="stars">★★★★☆</div>
    </div>
  </div>
</section>

<h2 class="blog-title">LATEST <em>BLOG</em></h2>
<article class="post" style="left:132px">
  <div class="post-photo" role="img" aria-label="Warehouse workers in safety vests checking stock" style="background:linear-gradient(160deg,#b8875a,#6a5a4a 60%,#c7b27a)"></div>
  <div class="post-body"><h3>Nemo enim ipsam voluptatem</h3>
    <div class="post-meta"><svg width="12" height="12" viewBox="0 0 12 12"><circle cx="6" cy="6" r="5" fill="none" stroke="#8a9099" stroke-width="1.4"/><path d="M6 3v3l2 1.5" fill="none" stroke="#8a9099" stroke-width="1.4"/></svg>3 minutes ago, 0 comments</div>
    <p>Lorem ipsum dolor sit amet, consectetur adipiscing elit, sed do eiusmod tempor incididunt</p></div>
</article>
<article class="post" style="left:455px">
  <div class="post-photo" role="img" aria-label="Hands holding a tablet with a chart" style="background:linear-gradient(160deg,#d9dde2,#7c8794 60%,#3d4651)"></div>
  <div class="post-body"><h3>Nemo enim ipsam voluptatem</h3>
    <div class="post-meta"><svg width="12" height="12" viewBox="0 0 12 12"><circle cx="6" cy="6" r="5" fill="none" stroke="#8a9099" stroke-width="1.4"/><path d="M6 3v3l2 1.5" fill="none" stroke="#8a9099" stroke-width="1.4"/></svg>3 minutes ago, 0 comments</div>
    <p>Lorem ipsum dolor sit amet, consectetur adipiscing elit, sed do eiusmod tempor incididunt</p></div>
</article>
<article class="post" style="left:775px">
  <div class="post-photo" role="img" aria-label="Tablet showing a warehouse interior" style="background:linear-gradient(160deg,#2d5f9e,#6f8fb8 55%,#b78a5a)"></div>
  <div class="post-body"><h3>Nemo enim ipsam voluptatem</h3>
    <div class="post-meta"><svg width="12" height="12" viewBox="0 0 12 12"><circle cx="6" cy="6" r="5" fill="none" stroke="#8a9099" stroke-width="1.4"/><path d="M6 3v3l2 1.5" fill="none" stroke="#8a9099" stroke-width="1.4"/></svg>3 minutes ago, 0 comments</div>
    <p>Lorem ipsum dolor sit amet, consectetur adipiscing elit, sed do eiusmod tempor incididunt</p></div>
</article>

<section class="search">
  <h2>STORAGE IN BODEGA</h2>
  <div class="field" style="top:196px">City</div>
  <div class="field" style="top:264px">Number of Pallets *</div>
  <div class="btn-solid">Search</div>
</section>
<div class="map" role="img" aria-label="Street map with red markers for available storage locations"></div>

<div class="partner" style="left:162px;width:168px"><i></i>Themora</div>
<div class="partner" style="left:350px;width:154px"><i></i>Activio</div>
<div class="partner" style="left:524px;width:168px"><i></i>Codewell</div>
<div class="partner" style="left:702px;width:168px"><i></i>Vidmora</div>
<div class="partner" style="left:884px;width:168px"><i></i>Themora</div>

<footer class="footer">
  <div class="brand">
    <span class="brand-mark"></span>
    <div><div class="brand-name">VORDEN</div><div class="brand-tag">ON-DEMAND WAREHOUSING</div></div>
  </div>
  <p class="footer-about">Sed ut perspiciatis unde omnis iste natus error sit voluptatem accusantium doloremque laudantium, totam rem aperiam, eaque ipsa quae ab illo inventore veritatis et quasi architecto beatae vitae dicta sunt explicabo. Nemo enim ipsam</p>
  <h4 class="col-title" style="left:504px">Contact Us</h4>
  <ul class="contact">
    <li><svg width="14" height="16" viewBox="0 0 14 16"><path d="M7 16C2 10 1 8 1 6a6 6 0 0 1 12 0c0 2-1 4-6 10z" fill="#c9ccd1"/><circle cx="7" cy="6" r="2" fill="#121316"/></svg><span>Vorden<br>48, 2210 R4, Halvern</span></li>
    <li><svg width="14" height="14" viewBox="0 0 14 14"><path d="M3 1l3 3-2 2c1 2 2 3 4 4l2-2 3 3-2 2C6 13 1 8 1 3z" fill="#c9ccd1"/></svg><span>Phone: (555) 014 207</span></li>
    <li><svg width="14" height="12" viewBox="0 0 14 12"><rect x="1" y="1" width="12" height="10" fill="none" stroke="#c9ccd1" stroke-width="1.4"/><path d="M1 1l6 5 6-5" fill="none" stroke="#c9ccd1" stroke-width="1.4"/></svg><span>enquiries@vorden-example.com</span></li>
    <li><svg width="14" height="14" viewBox="0 0 14 14"><circle cx="7" cy="7" r="6" fill="none" stroke="#c9ccd1" stroke-width="1.4"/><path d="M7 3v4l3 2" fill="none" stroke="#c9ccd1" stroke-width="1.4"/></svg><span>9:00am – 5:00pm</span></li>
  </ul>
  <h4 class="col-title" style="left:778px">Quick Links</h4>
  <ul class="links"><li>Home</li><li>Solutions</li><li>Company</li><li>Blog</li><li>Sign In</li><li>Contact Us</li></ul>
  <h4 class="col-title" style="left:960px">Follow Us</h4>
  <ul class="social"><li><i></i>Friendlo</li><li><i></i>Chirpa</li><li><i></i>Circlet</li><li><i></i>Tubeo</li></ul>
  <div class="footer-rule"></div>
  <p class="copyright">© Copyright 2018 Vorden. All Rights Reserved. Terms and Conditions | Privacy Policy</p>
</footer>

<div class="newsletter" role="region" aria-label="Newsletter signup">
  <h2>Join our Newsletter</h2>
  <p>Subscribe to our mailing list to receive updates and promotional offers</p>
  <div class="subscribe"><span>Enter your E - mail</span><b>SUBSCRIBE</b></div>
</div>
<div class="ad-slot">Ad<br>Banners</div>

</body>
</html>
```